Ledge Span Services

Hi there. this is Kaveh.
I requested a design a few months ago and got a good design and designer but didn't come to reality when I send it for print.
So I kind of change my mind and going on the easier way which is the double-sided business card
I'll upload the previous design which needs a few small changes to put a background on it and need the second side of the card to be kind of same design with the pressure wash in the rope.

1. window cleaning side
Please find nice city background and clear area want it to be a sky blue,
*make sure the city color make the writing easy to read
*that clear area is the main part of the design!
Writing
"-Window Cleaning
Friendly, Reliable & Professional Team
Experienced Residential & Commercial service
We clean any window up to 50 Stories
Free quotes & can often do over the phone using Mapsly
0481736205
contact@ledgespanservices.example
www.ledgespanservices.example
PO Box 312 Albury 2640 NSW"

2. Please design the same kind of idea but with the pressure washing on the rope. Shadow prefer
writing :

"HighRise Pressure Washing
Solar Panel Cleaning
House/Building Washing
Roof/Floor Cleaning
Free quotes

0481736205

```html
<!DOCTYPE html>
<html lang="en">
<head>
<meta charset="utf-8">
<title>Ledge Span Services – Business Card</title>
<link rel="stylesheet" href="https://fonts.googleapis.com/css2?family=Arvo:ital,wght@0,400;0,700;1,700&display=swap">
<style>
  :root {
    --page-bg: #e4e4e4;
    --card-light: #f3f3f3;
    --brand-blue: #00adef;
    --ink: #111111;
    --skyline: #0a8fcc;
    --figure-dark: #1a1a1a;
    --bullet: #00adef;
    --logo-green: #7dc242;
  }
  * { box-sizing: border-box; margin: 0; padding: 0; }
  html, body {
    width: 1156px; height: 1200px; overflow: hidden;
    background: var(--page-bg);
    font-family: "Arvo", Georgia, serif;
    color: var(--ink);
  }
  .card {
    position: absolute; left: 222px; width: 695px; height: 396px; overflow: hidden;
  }
  .card--front { top: 153px; background: var(--card-light); }
  .card--back { top: 607px; background: var(--brand-blue); }

  /* Front */
  .services {
    position: absolute; left: 42px; top: 38px; list-style: none;
    font-size: 15px; line-height: 28px;
  }
  .services li { position: relative; padding-left: 14px; }
  .services li::before {
    content: ""; position: absolute; left: 0; top: 12px;
    width: 4px; height: 4px; border-radius: 50%; background: var(--bullet);
  }
  .services .two-line { line-height: 20px; padding-top: 4px; padding-bottom: 4px; }
  .services .two-line::before { top: 8px; }

  .contact-band {
    position: absolute; left: 0; top: 255px; width: 350px; height: 76px;
    background: var(--brand-blue);
    padding: 10px 0 0 42px; font-size: 14.5px; line-height: 19.5px;
  }
  .front-address { position: absolute; left: 42px; top: 350px; font-size: 14.5px; }

  .brand-name {
    position: absolute; left: 452px; top: 38px;
    display: flex; align-items: center; gap: 10px;
    font-size: 25px; line-height: 32px; color: var(--brand-blue);
  }
  .brand-name .mark { flex: none; width: 14px; height: 14px; background: var(--logo-green); }

  .climber-art {
    position: absolute; left: 372px; top: 122px; width: 150px; height: 274px;
    border-radius: 40px 40px 0 0;
    background: linear-gradient(180deg, rgba(26,26,26,0.35) 0%, var(--figure-dark) 30%, var(--figure-dark) 75%, rgba(26,26,26,0.4) 100%);
  }

  /* Back */
  .skyline-art {
    position: absolute; left: 0; right: 0; bottom: 0; height: 262px;
    background: linear-gradient(180deg, rgba(10,143,204,0) 0%, rgba(10,143,204,0.55) 55%, var(--skyline) 100%);
  }
  .back-content {
    position: absolute; left: 0; right: 0; top: 64px; text-align: center;
    font-size: 14.5px; line-height: 20px;
  }
  .back-title { font-size: 32px; line-height: 40px; font-weight: 400; }
  .quote-note { margin-top: 38px; font-weight: 700; font-style: italic; line-height: 19px; }
  .rule { width: 38px; height: 1px; background: var(--ink); margin: 6px auto; }
</style>
</head>
<body>
  <section class="card card--front" aria-label="Card front">
    <ul class="services">
      <li>HighRise Pressure Washing</li>
      <li>Solar Panel Cleaning</li>
      <li>House/Building Washing</li>
      <li>Roof/Floor Cleaning</li>
      <li class="two-line">Experienced Residential &amp;<br>Commercial service</li>
      <li>Free quotes</li>
    </ul>
    <div class="contact-band">
      <p>0481736205</p>
      <p>contact@ledgespanservices.example</p>
      <p>www.ledgespanservices.example</p>
    </div>
    <p class="front-address">PO Box 312 Albury 2640 NSW</p>
    <div class="brand-name"><span class="mark"></span><span>Ledge Span<br>Services</span></div>
    <div class="climber-art" role="img" aria-label="Silhouette of a worker on ropes pressure washing a building"></div>
  </section>

  <section class="card card--back" aria-label="Card back">
    <div class="skyline-art" role="img" aria-label="Faint city skyline silhouette along the bottom"></div>
    <div class="back-content">
      <h1 class="back-title">Window Cleaning</h1>
      <p>Friendly, Reliable &amp; Professional Team</p>
      <p>Experienced Residential &amp; Commercial service</p>
      <p>We clean any window up to 50 Stories</p>
      <p class="quote-note">Free quotes &amp; can often do<br>over the phone using Mapsly</p>
      <div class="rule"></div>
      <p>Cell : 0481736205</p>
      <p>contact@ledgespanservices.example</p>
      <p>www.ledgespanservices.example</p>
      <div class="rule"></div>
      <p>PO Box 312 Albury 2640 NSW</p>
    </div>
  </section>
</body>
</html>
```